Interior design service, along with home organization, packing, and staging, home and business. As well as staging in conjunction with real estate sales.

Love many of your designs and will be choosing today. To inform you of the exact details needed, the name of the company is "Flourish by Marnie T" , my phone number and e-,ail need to be included. i also need either description or some sort of bullet points that give an idea of the following:

- Interior design for home and business
- Home organization and packing
- Staging for personal and professional space
- Real estate stagingĀ 

Thank you

Target Market(s)

wide audience, but most importantly people looking for a quality service

Industry/Entity Type

Real Estate

Contact Information for Business Card

Flourish By Marnie T
Marnie Toller
(555)617-3942
mtbriar@inboxly.example

Requirements
Must have
• I'm 29 so i want my card to reflect something professional but still fresh. I don't have any specific photos or quotes that Ive included, however I like the card to reflect a personal touch, which is what I'm seeking from this service in the design of my card. Thanks!

```html
<!DOCTYPE html>
<html lang="en">
<head>
<meta charset="utf-8">
<title>Flourish by Marnie T – Business Card</title>
<link rel="stylesheet" href="https://fonts.googleapis.com/css2?family=Mulish:wght@400;600;800&display=swap">
<style>
  :root {
    --page: #ffffff;
    --card-black: #000000;
    --pattern-dark: #0c0c0c;
    --pattern-mid: #2a2a2a;
    --gold: #c9a13c;
    --gold-light: #e6c56a;
    --text-white: #f2f2f2;
    --text-grey: #c8c8c8;
    --text-muted: #a9a9a9;
  }
  html, body {
    margin: 0;
    padding: 0;
    width: 1200px;
    height: 900px;
    overflow: hidden;
    background: var(--page);
  }
  .canvas {
    position: relative;
    width: 1200px;
    height: 900px;
  }
  .card {
    position: absolute;
    top: 277px;
    width: 584px;
    height: 341px;
    background: var(--card-black);
    box-sizing: border-box;
    overflow: hidden;
  }
  .card--front { left: 9px; }
  .card--back  { left: 606px; }

  .front-pattern {
    position: absolute;
    inset: 0;
    background: radial-gradient(ellipse at 50% 50%, var(--pattern-mid) 0%, var(--pattern-dark) 75%);
  }
  .frame-outer {
    position: absolute;
    inset: 6px;
    border: 4px solid var(--gold);
  }
  .frame-inner {
    position: absolute;
    inset: 15px;
    border: 2px solid var(--gold-light);
  }
  .brand-name {
    position: absolute;
    inset: 0;
    display: flex;
    flex-direction: column;
    align-items: center;
    justify-content: center;
    margin: 0;
    font-family: "Mulish", sans-serif;
    font-weight: 800;
    font-size: 64px;
    line-height: 1.2;
    letter-spacing: 2px;
    text-transform: uppercase;
    color: var(--gold);
  }

  .contact {
    position: absolute;
    top: 102px;
    left: 0;
    right: 0;
    font-family: "Mulish", sans-serif;
    text-align: center;
  }
  .contact-name {
    margin: 0 0 34px;
    font-weight: 600;
    font-size: 24px;
    line-height: 30px;
    color: var(--gold);
  }
  .contact-phone {
    margin: 0 0 4px;
    font-weight: 400;
    font-size: 24px;
    line-height: 30px;
    color: var(--text-white);
  }
  .contact-email {
    margin: 0;
    font-weight: 400;
    font-size: 24px;
    line-height: 30px;
    color: var(--text-grey);
  }
  .services {
    position: absolute;
    top: 250px;
    left: 0;
    right: 0;
    margin: 0;
    padding: 0;
    list-style: none;
    font-family: "Mulish", sans-serif;
    font-weight: 400;
    font-size: 14px;
    line-height: 19px;
    text-align: center;
    color: var(--text-muted);
  }
  .service::before {
    content: "";
    display: inline-block;
    width: 5px;
    height: 5px;
    margin: 0 8px 3px 0;
    background: var(--gold);
    vertical-align: middle;
  }
</style>
</head>
<body>
<main class="canvas">
  <section class="card card--front">
    <div class="front-pattern" role="img" aria-label="Dark black damask swirl pattern background"></div>
    <div class="frame-outer"></div>
    <div class="frame-inner"></div>
    <h1 class="brand-name">
      <span>Flourish</span>
      <span>By</span>
      <span>Marnie T</span>
    </h1>
  </section>

  <section class="card card--back">
    <div class="contact">
      <p class="contact-name">Marnie Toller</p>
      <p class="contact-phone">(555)617-3942</p>
      <p class="contact-email">mtbriar@inboxly.example</p>
    </div>
    <ul class="services">
      <li class="service">Interior design for home and business</li>
      <li class="service">Home organization and packing</li>
      <li class="service">Staging for personal and professional space</li>
      <li class="service">Real estate staging</li>
    </ul>
  </section>
</main>
</body>
</html>
```